Website design and Setup for Real Estate Firm and Going Live

We are a commercial real estate investment firm and are looking for a 6 page website which is informational only. Some text and graphics on each page. We would want the designer to code and launch the website. This website needs to be corporate looking as well as innovative. We are setting up the website on webnook.

The first page will be a home page with generic commercial real estate look with a link to the following 5 pages on page 1. So page one (the Home Page should have a commercial real estate look with the text linking to the following pages. Page 2 "About Us" with 3 paragraphs describing our firm. Page 3 "Our Platform" with another few paragraphs on due diligence, acquisitions, financing, and management.

Page 4 is "Our Team" highlighting several manager profiles. Page 5 is our "investment Portfolio portal" which will be password protected so not a lot of text, only general graphics and anyone viewing the site casually won't get into the backend, Page 6 is the contact us page. All of the content will be uploaded shortly.

The project includes setting up hyperlinks in the website as well rotating images etc and a final complete live online product. We do not expect to pay for any stock images.

Target Market(s)

Investors, Real Estate Professionals, Brokerages

Industry/Entity Type

Real Estate

Coding

Coded - Design and coding required

Number of Pages Required

5+ page

Requirements
Must have
• Corporate cutting edge design, suitable for a financial corporation.

```html
<!DOCTYPE html>
<html lang="en">
<head>
<meta charset="utf-8">
<title>Hale Morrow Realty</title>
<link rel="stylesheet" href="https://fonts.googleapis.com/css2?family=Rubik:wght@500;700&family=Roboto:wght@300;400;500;700&display=swap">
<style>
:root{
  --brand:#b06d28;
  --ink:#111318;
  --text:#666a70;
  --soft:#f0f1f3;
  --night:#0e1117;
  --white:#ffffff;
  --sky-1:#1f5fae;
  --sky-2:#6ea6e0;
}
*{box-sizing:border-box;margin:0;padding:0}
html,body{width:1200px;height:3003px;overflow:hidden}
body{position:relative;font-family:"Roboto",sans-serif;color:var(--ink);background:var(--white)}
.abs{position:absolute}
.display{font-family:"Rubik",sans-serif;font-weight:700;text-transform:uppercase}
.btn{position:absolute;display:flex;align-items:center;justify-content:center;gap:10px;background:var(--brand);color:var(--white);font-family:"Rubik",sans-serif;font-weight:500;font-size:15px;text-transform:uppercase;border-radius:3px}
.btn svg{width:14px;height:14px}

/* header */
.site-header{position:absolute;left:0;top:0;width:1200px;height:76px;background:var(--white);z-index:3}
.main-nav{position:absolute;left:361px;top:27px;display:flex;gap:31px;font-size:15.5px;color:#333}
.search-btn{position:absolute;left:845px;top:20px;width:32px;height:32px;border-radius:50%;background:var(--brand);display:flex;align-items:center;justify-content:center}
.login-btn{left:924px;top:15px;width:117px;height:42px}
.brand-badge{position:absolute;left:160px;top:28px;width:154px;height:126px;border-radius:0 0 77px 77px;background:var(--white);z-index:4;display:flex;align-items:flex-end;justify-content:center;padding-bottom:34px}
.brand-badge span{font-family:"Rubik",sans-serif;font-weight:500;font-size:11.5px;color:var(--ink);text-align:center;line-height:1.25;white-space:nowrap}

/* hero */
.hero-photo{left:0;top:76px;width:1200px;height:570px;background:linear-gradient(160deg,#0d2f66 0%,var(--sky-1) 35%,var(--sky-2) 60%,#1a4d93 85%,#0a2550 100%)}
.hero-card{left:635px;top:233px;width:451px;height:255px;background:rgba(60,66,74,.9);text-align:center;color:var(--white)}
.hero-card h1{margin-top:49px;font-size:33px}
.hero-card p{margin-top:14px;font-size:15.5px;line-height:26px;font-weight:300}
.hero-cta{left:131px;top:170px;width:169px;height:47px}
.scroll-cue{left:580px;top:630px;width:42px;height:42px;border-radius:50%;background:var(--white);border:2px solid #e5e5e5;display:flex;align-items:center;justify-content:center}

/* about */
.eyebrow{color:var(--brand);font-size:25px}
.about-eyebrow{left:111px;top:733px}
.about-title{left:111px;top:772px;font-size:29px;line-height:33px}
.about-quote{left:111px;top:860px;width:480px;border-left:3px solid var(--brand);padding-left:19px;font-size:15.5px;line-height:26px;color:var(--text);white-space:nowrap}
.about-copy{left:111px;top:928px;width:500px;font-size:15.5px;line-height:25.7px;color:var(--text)}
.about-btn{left:111px;top:1073px;width:165px;height:47px}
.about-photo-building{left:700px;top:739px;width:393px;height:382px;background:linear-gradient(180deg,#cfd6dc 0%,#5b6470 45%,#3a3e44 75%,#8a8477 100%)}
.about-photo-portrait{left:647px;top:969px;width:163px;height:152px;background:linear-gradient(135deg,#2a3a5a,#16213a)}

/* approach */
.approach{left:0;top:1216px;width:1200px;height:520px;background:var(--soft)}
.center-title{width:1200px;left:0;text-align:center}
.approach-card{top:1383px;height:285px;color:var(--white);font-family:"Rubik",sans-serif;font-weight:700;font-size:15px;text-transform:uppercase}
.approach-card .label{position:absolute;left:0;right:0;bottom:24px;text-align:center}
.card-acq{left:107px;width:235px;background:linear-gradient(160deg,#dfe8f2,#6f8fb3 55%,#2f4866)}
.card-dev{left:358px;width:234px;background:linear-gradient(160deg,#d19a55,#a86a2b);border:3px solid var(--brand)}
.card-dev .overlay{position:absolute;left:17px;top:17px;width:195px;height:245px;background:rgba(198,136,70,.88);padding:33px 19px 0;font-weight:500}
.card-dev p{margin-top:14px;font-family:"Roboto",sans-serif;font-weight:300;font-size:15.5px;line-height:26px;text-transform:none}
.card-dev .go{margin-top:14px;width:28px;height:28px;border-radius:50%;background:var(--white);display:flex;align-items:center;justify-content:center}
.card-fin{left:607px;width:235px;background:linear-gradient(180deg,#6ea6de 0%,#9ab8d2 35%,#55606c 65%,#6f8c4a 100%)}
.card-asset{left:858px;width:235px;background:linear-gradient(180deg,#7aa6d6 0%,#4f7aa8 45%,#2c3e55 100%)}

/* how it works */
.role-card{top:1937px;width:198px;height:169px;background:var(--brand);color:var(--white);border-radius:2px;text-align:center}
.role-card svg{margin-top:28px;width:90px;height:80px}
.role-card span{display:block;margin-top:12px;font-family:"Rubik",sans-serif;font-weight:700;font-size:16px;text-transform:uppercase}

/* contact */
.contact{left:0;top:2190px;width:1200px;height:485px;background:var(--soft)}
.contact-item{left:110px;display:flex;gap:14px}
.contact-icon{width:36px;height:36px;border-radius:50%;border:1.5px solid var(--brand);display:flex;align-items:center;justify-content:center;flex:none;margin-top:4px}
.contact-item b{display:block;font-size:13.5px;font-weight:500}
.contact-item p{font-size:16.5px;line-height:23px;color:#333;margin-top:3px}
.follow{left:111px;top:2552px;font-family:"Rubik",sans-serif;font-weight:700;font-size:17px}
.socials{left:111px;top:2586px;display:flex;gap:11px}
.socials i{width:29px;height:29px;border-radius:50%;border:1.5px solid var(--brand)}
.form-accent{left:923px;top:2283px;width:134px;height:125px;background:var(--brand)}
.contact-form{left:542px;top:2318px;width:467px;height:383px;background:var(--white);box-shadow:0 2px 12px rgba(0,0,0,.06);z-index:2}
.field{position:absolute;border:1px solid #cfcfcf;font-size:10.5px;color:#333;padding:10px 7px}
.consent{position:absolute;left:85px;top:256px;display:flex;gap:9px;align-items:center;font-size:10.5px;color:#333}
.consent i{width:15px;height:15px;border:1px solid #777}
.submit{left:174px;top:284px;width:121px;height:41px}

/* footer */
.site-footer{left:0;top:2675px;width:1200px;height:328px;background:var(--night);color:var(--white);text-align:center}
.footer-mark{position:absolute;left:577px;top:105px;width:46px;height:46px;background:var(--brand)}
.footer-name{position:absolute;left:0;width:1200px;top:172px;font-family:"Rubik",sans-serif;font-weight:500;font-size:16px;text-transform:uppercase}
.footer-nav{position:absolute;left:0;width:1200px;top:223px;display:flex;justify-content:center;gap:32px;font-size:16.5px}
.footer-rule{position:absolute;left:111px;top:273px;width:978px;height:1px;background:#3a3d44}
.copyright{position:absolute;left:0;width:1200px;top:290px;font-size:14.5px}
</style>
</head>
<body>

<header class="site-header">
  <nav class="main-nav"><span>HOME</span><span>ABOUT US</span><span>SERVICES</span><span>BLOG</span><span>CONTACT US</span></nav>
  <div class="search-btn"><svg width="14" height="14" viewBox="0 0 14 14"><circle cx="6" cy="6" r="4.2" fill="none" stroke="#fff" stroke-width="2"/><path d="M9 9l3.5 3.5" stroke="#fff" stroke-width="2"/></svg></div>
  <div class="btn login-btn">Login <svg viewBox="0 0 14 14"><path d="M1 7h8M6 4l3 3-3 3" stroke="#fff" stroke-width="2" fill="none"/><path d="M9 1h4v12H9" stroke="#fff" stroke-width="1.6" fill="none"/></svg></div>
</header>
<div class="brand-badge"><span>HALE MORROW REALTY</span></div>

<section>
  <div class="abs hero-photo" role="img" aria-label="Skyscrapers viewed from below against a blue sky"></div>
  <div class="abs hero-card">
    <h1 class="display">Hale Morrow Realty</h1>
    <p>Lorem ipsum dolor sit consectetur adipeiusmod<br>tempor incididunt ut labore et dolore magna.</p>
    <div class="btn hero-cta">Get Started <svg viewBox="0 0 14 14"><circle cx="7" cy="7" r="6.5" fill="#fff"/><path d="M6 4l3 3-3 3" stroke="#b06d28" stroke-width="1.8" fill="none"/></svg></div>
  </div>
  <div class="abs scroll-cue"><svg width="14" height="16" viewBox="0 0 14 16"><path d="M7 1v12M2 8l5 5 5-5" stroke="#b06d28" stroke-width="2.4" fill="none"/></svg></div>
</section>

<section>
  <h2 class="abs display eyebrow about-eyebrow">About Us</h2>
  <h3 class="abs display about-title">Perspiciatis unde<br>omnis iste natus</h3>
  <p class="abs about-quote">Lorem ipsum dolor sit amet, consectetur adipiscing elit, sed<br>do eiusmod tempor incididunt ut labore et dolore magna</p>
  <p class="abs about-copy">Lorem ipsum dolor sit amet, consectetur adipiscing eiusmod tempor incididunt ut labore et dolore magna aliqua.Ut enim ad minim veniam, quis nostrud exercitation ullamco laboris nisi ut aliquip ex ea commod conseqaute irure dolor in reprehenderit voluptate velit esse cillummd olore eu fugiat nulla pariatur. veritatis et quasi architecto beatae vitae</p>
  <div class="btn about-btn">Learn More <svg viewBox="0 0 14 14"><circle cx="7" cy="7" r="6.5" fill="#fff"/><path d="M6 4l3 3-3 3" stroke="#b06d28" stroke-width="1.8" fill="none"/></svg></div>
  <div class="abs about-photo-building" role="img" aria-label="Modern glass office building at dusk"></div>
  <div class="abs about-photo-portrait" role="img" aria-label="Portrait of the firm's principal"></div>
</section>

<section>
  <div class="abs approach"></div>
  <h2 class="abs display eyebrow center-title" style="top:1280px">Our Approach</h2>
  <h3 class="abs display center-title" style="top:1318px;font-size:29px">Lorem ipsum dolor&nbsp; amet</h3>
  <div class="abs approach-card card-acq" role="img" aria-label="Glass office towers"><span class="label">Acquisition</span></div>
  <div class="abs approach-card card-dev" role="img" aria-label="Apartment tower facade">
    <div class="overlay">Development
      <p>Lorem ipsum dolor sit consectetur adipiscing elit, sed do eiusmod</p>
      <div class="go"><svg width="12" height="12" viewBox="0 0 12 12"><path d="M1 6h9M6 2l4 4-4 4" stroke="#b06d28" stroke-width="2" fill="none"/></svg></div>
    </div>
  </div>
  <div class="abs approach-card card-fin" role="img" aria-label="Office campus with lawn"><span class="label">Financing</span></div>
  <div class="abs approach-card card-asset" role="img" aria-label="City skyline towers"><span class="label">Asset Management</span></div>
</section>

<section>
  <h2 class="abs display eyebrow center-title" style="top:1816px">How Its Work</h2>
  <h3 class="abs display center-title" style="top:1857px;font-size:29px">Lorem ipsum dolor&nbsp; amet</h3>
  <div class="abs role-card" style="left:166px">
    <svg viewBox="0 0 90 80" fill="none" stroke="#fff" stroke-width="4"><rect x="8" y="6" width="44" height="70"/><rect x="52" y="30" width="30" height="46"/><path d="M16 18h10v10H16zM34 18h10v10H34zM16 38h10v10H16zM34 38h10v10H34zM22 76V62a8 8 0 0116 0v14M58 40h18M58 50h18M58 60h18"/></svg>
    <span>Owner</span></div>
  <div class="abs role-card" style="left:389px">
    <svg viewBox="0 0 90 80" fill="none" stroke="#fff" stroke-width="4"><rect x="12" y="28" width="28" height="46"/><rect x="40" y="6" width="36" height="68"/><path d="M4 76h82M18 38h6M28 38h6M18 50h6M28 50h6M18 62h6M28 62h6M48 16h8M62 16h8M48 30h8M62 30h8M48 44h8M62 44h8M48 58h8M62 58h8"/></svg>
    <span>Developer</span></div>
  <div class="abs role-card" style="left:612px">
    <svg viewBox="0 0 90 80" fill="#fff"><path d="M24 4h42v74H24zM6 34h14v44H6zM70 34h14v44H70z"/><g fill="#b06d28"><rect x="31" y="12" width="8" height="8"/><rect x="51" y="12" width="8" height="8"/><rect x="31" y="28" width="8" height="8"/><rect x="51" y="28" width="8" height="8"/><rect x="31" y="44" width="8" height="8"/><rect x="51" y="44" width="8" height="8"/><rect x="39" y="62" width="12" height="16"/></g></svg>
    <span>Investor</span></div>
  <div class="abs role-card" style="left:836px">
    <svg viewBox="0 0 90 80" fill="none" stroke="#fff" stroke-width="4"><path d="M8 76V28l24-8v56M32 76V14l26-10v72M58 76V26l24 6v44M4 77h82M12 36h16M12 46h16M12 56h16M12 66h16M36 22h18M36 32h18M36 42h18M36 52h18M36 62h18M62 40h16M62 50h16M62 60h16"/></svg>
    <span>Operator</span></div>
</section>

<section>
  <div class="abs contact"></div>
  <h2 class="abs display eyebrow" style="left:110px;top:2246px">Contact Info</h2>
  <h3 class="abs display" style="left:110px;top:2282px;font-size:29px">Get in touch with us</h3>
  <div class="abs contact-item" style="top:2333px">
    <div class="contact-icon"><svg width="14" height="14" viewBox="0 0 14 14"><path d="M3 1l2.5 3-1.5 1.5a8 8 0 004.5 4.5L10 8.5l3 2.5-1.5 2C6 13 1 8 1 2.5z" fill="#b06d28"/></svg></div>
    <div><b>Phone Number :</b><p>123 (456) 789</p></div></div>
  <div class="abs contact-item" style="top:2397px">
    <div class="contact-icon"><svg width="15" height="12" viewBox="0 0 15 12"><rect x="0.5" y="1" width="14" height="10" rx="1" fill="#b06d28"/><path d="M1 2l6.5 5L14 2" stroke="#fff" stroke-width="1.3" fill="none"/></svg></div>
    <div><b>Email :</b><p>info@halemorrowrealty.com</p></div></div>
  <div class="abs contact-item" style="top:2461px">
    <div class="contact-icon" style="margin-top:20px"><svg width="12" height="16" viewBox="0 0 12 16"><path d="M6 0a6 6 0 00-6 6c0 4.5 6 10 6 10s6-5.5 6-10a6 6 0 00-6-6z" fill="#b06d28"/><circle cx="6" cy="6" r="2.3" fill="#fff"/></svg></div>
    <div><b>Address :</b><p>perspiciatis unde omnis iste natus error<br>sit voluptatem accusantium doloremque</p></div></div>
  <div class="abs follow">FOLLOW US</div>
  <div class="abs socials"><i></i><i></i><i></i><i></i></div>

  <div class="abs form-accent"></div>
  <form class="abs contact-form">
    <div class="field" style="left:49px;top:58px;width:180px;height:34px">First Name:</div>
    <div class="field" style="left:241px;top:58px;width:179px;height:34px">Email:</div>
    <div class="field" style="left:49px;top:110px;width:180px;height:34px">Phone Number:</div>
    <div class="field" style="left:241px;top:110px;width:179px;height:34px">Address:</div>
    <div class="field" style="left:49px;top:163px;width:371px;height:70px">Message:</div>
    <div class="consent"><i></i>perspiciatis unde omnis iste natus error sit voluptatem a</div>
    <div class="btn submit">Submit <svg viewBox="0 0 14 14"><circle cx="7" cy="7" r="6.5" fill="#fff"/><path d="M3.5 7l7-3-2 7-1.5-2.5z" fill="#b06d28"/></svg></div>
  </form>
</section>

<footer class="abs site-footer">
  <div class="footer-mark"></div>
  <div class="footer-name">Hale Morrow Realty</div>
  <nav class="footer-nav"><span>HOME</span><span>ABOUT US</span><span>SERVICE</span><span>BLOG</span><span>CONTACT US</span></nav>
  <div class="footer-rule"></div>
  <p class="copyright">©Copyrights 2021&nbsp; Hale Morrow Realty&nbsp; |&nbsp;&nbsp; All Rights Reserved&nbsp; |</p>
</footer>

</body>
</html>
```